CRPG is needing business cards, and stationary created.

Pixel Forge created a logo for our business, and now we are wanting business cards, and stationary. I have included two designs of the same logo. Please feel free to use them as you want. The name of the company is Cedar Ridge Property Group LLC, the address is 812 NE Willow Ln., Suite 9, the city & state is Bend, Oregon, zip code is 97815, Telephone number is 541-327-4489, Fax number is 541-327-6051, the name on the business card is Carl Whitby CMCA

Industry/Entity Type

Property Management

Contact Information for Business Card

The card needs to look professional. Upscale.

Requirements
Must have
• The colors we are using are on the logo that has been uploaded.

```html
<!DOCTYPE html>
<html lang="en">
<head>
<meta charset="utf-8">
<title>Cedar Ridge Property Group – Business Card</title>
<link href="https://fonts.googleapis.com/css2?family=Work+Sans:wght@400;500;700&display=swap" rel="stylesheet">
<style>
  :root {
    --backdrop: #9a9c9f;
    --slate: #3b4a5c;
    --slate-deep: #34414f;
    --teal: #17907a;
    --ink: #2f3a4a;
    --rule: #5a6573;
    --paper: #ffffff;
  }
  * { box-sizing: border-box; margin: 0; padding: 0; }
  html, body {
    width: 1200px; height: 930px; overflow: hidden;
    background: var(--backdrop);
    font-family: "Work Sans", Arial, sans-serif;
  }
  .stage { position: relative; width: 1200px; height: 930px; }

  .card {
    position: absolute;
    width: 580px; height: 331px;
    border-radius: 22px;
    overflow: hidden;
    box-shadow: 0 10px 24px rgba(0,0,0,.22);
  }

  /* Back side */
  .card-back { left: 80px; top: 90px; background: var(--slate); }
  .card-back .pattern-area {
    position: absolute; inset: 0;
    background: linear-gradient(135deg, var(--slate) 0%, var(--slate-deep) 100%);
  }
  .card-back .brand {
    position: absolute; left: 150px; top: 210px;
    display: flex; align-items: center; gap: 12px;
  }
  .card-back .brand-mark { width: 30px; height: 30px; background: var(--paper); }
  .card-back .brand-name {
    color: var(--paper); font-weight: 700; font-size: 24px; letter-spacing: .5px;
  }

  /* Front side */
  .card-front { left: 540px; top: 500px; background: var(--paper); }
  .card-front .brand {
    position: absolute; left: 40px; top: 100px;
    display: flex; align-items: center; gap: 12px;
  }
  .card-front .brand-mark { width: 30px; height: 30px; background: var(--slate); }
  .card-front .brand-name {
    color: var(--teal); font-weight: 700; font-size: 27px; letter-spacing: .5px;
  }

  .holder { position: absolute; right: 44px; top: 92px; text-align: right; }
  .holder-name {
    color: var(--ink); font-weight: 500; font-size: 24px; letter-spacing: .8px;
    text-transform: uppercase;
  }
  .holder-title { color: var(--teal); font-size: 14px; margin-top: 2px; letter-spacing: .5px; }

  .divider {
    position: absolute; left: 40px; right: 40px; top: 178px;
    height: 1px; background: var(--rule);
  }

  .address {
    position: absolute; right: 44px; top: 192px; text-align: right;
    color: var(--teal); font-size: 15px; line-height: 1.45;
  }

  .contacts { position: absolute; left: 40px; top: 192px; list-style: none; }
  .contacts li {
    display: flex; align-items: center; gap: 10px;
    color: var(--teal); font-size: 17px; line-height: 24px;
  }
  .contacts svg { width: 11px; height: 11px; flex: none; }

  .footer-band { position: absolute; left: 0; bottom: 0; width: 580px; height: 70px; }
</style>
</head>
<body>
<main class="stage">

  <section class="card card-back" aria-label="Business card, back">
    <div class="pattern-area" role="img" aria-label="Tone-on-tone slate repeating pattern covering the card"></div>
    <div class="brand">
      <span class="brand-mark"></span>
      <span class="brand-name">CEDAR RIDGE</span>
    </div>
  </section>

  <section class="card card-front" aria-label="Business card, front">
    <div class="brand">
      <span class="brand-mark"></span>
      <span class="brand-name">CEDAR RIDGE</span>
    </div>

    <div class="holder">
      <div class="holder-name">Carl Whitby</div>
      <div class="holder-title">CMCA</div>
    </div>

    <div class="divider"></div>

    <ul class="contacts">
      <li>
        <svg viewBox="0 0 12 12"><path d="M2.5 1l2 2.2-1 1.3c.7 1.5 1.6 2.4 3 3l1.3-1L10 8.5 9 10.5C5 10.3 1.7 7 1.5 3z" fill="var(--ink)"/></svg>
        541-327-4489
      </li>
      <li>
        <svg viewBox="0 0 12 12"><rect x="3" y="1" width="6" height="3" fill="var(--ink)"/><rect x="1" y="5" width="10" height="5" rx="1" fill="var(--ink)"/></svg>
        541-327-6051
      </li>
      <li>
        <svg viewBox="0 0 12 12"><rect x="1" y="2.5" width="10" height="7" fill="none" stroke="var(--ink)" stroke-width="1.2"/><path d="M1 2.5l5 4 5-4" fill="none" stroke="var(--ink)" stroke-width="1.2"/></svg>
        info@crpgllc.com
      </li>
      <li>
        <svg viewBox="0 0 12 12"><circle cx="6" cy="6" r="5" fill="none" stroke="var(--ink)" stroke-width="1.1"/><path d="M1 6h10M6 1c-2.5 3-2.5 7 0 10M6 1c2.5 3 2.5 7 0 10" fill="none" stroke="var(--ink)" stroke-width="1"/></svg>
        www.crpgllc.com
      </li>
    </ul>

    <div class="address">
      812 NE Willow Ln., Suite 9,<br>
      Bend, Oregon, 97815
    </div>

    <svg class="footer-band" viewBox="0 0 580 70" preserveAspectRatio="none" aria-hidden="true">
      <polygon points="0,58 360,58 360,70 0,70" fill="var(--teal)"/>
      <polygon points="372,12 580,12 580,70 372,70" fill="var(--slate)"/>
    </svg>
  </section>

</main>
</body>
</html>
```